Create a Powerpoint presentation pack with our new logo

We have just selected a new logo using PixelGuild and we were wanting to create a new Powerpoint presentation pack using this logo.
We'd like the powerpoint pack to have a title page + a header and footer page.
We would like the logo to appear on the title page and the header / footer page.
We are flexible with colours and want something that reflects an IT / travel flair.

I have attached the logo that we just selected from the pixelguild page.

Larkmoor Systems Division is the IT division of Larkmoor Voyage Holdings which is the largest travel retailer in Australia. We have offices in the US, Canada, UK, Singapore, Hong Kong, UAE, India, South Africa, Mexico and New Zealand.

```html
<!DOCTYPE html>
<html lang="en">
<head>
<meta charset="utf-8">
<title>Larkmoor Systems Division – Presentation Pack</title>
<link href="https://fonts.googleapis.com/css2?family=Raleway:wght@400;600;700;800&display=swap" rel="stylesheet">
<style>
:root{
  --red:#e8262c;
  --black:#121212;
  --dark:#2a2a2a;
  --mid:#4a4a4a;
  --gray:#7d7d7d;
  --silver:#a9a9a9;
  --light:#f1f1f1;
  --white:#ffffff;
  --text:#8a8a8a;
}
*{box-sizing:border-box;margin:0;padding:0}
html,body{width:902px;height:1200px;overflow:hidden;background:#fff}
body{font-family:"Raleway",Arial,sans-serif;color:var(--dark)}
.pack{display:grid;grid-template-columns:repeat(3,296px);grid-template-rows:repeat(7,165px);gap:6px 4px;padding:2px 1px;width:902px;height:1200px}
.slide{position:relative;overflow:hidden;background:var(--white);box-shadow:0 0 0 1px #e3e3e3}
.abs{position:absolute}
.fill{position:absolute;inset:0}
/* brand */
.brand{position:absolute;display:flex;align-items:center;gap:3px;color:var(--red);font-weight:800;letter-spacing:.3px}
.brand-mark{display:block;border:1.2px solid currentColor;border-radius:50%}
.brand.stack{flex-direction:column;gap:2px}
.brand-sm{font-size:4px}.brand-sm .brand-mark{width:7px;height:7px}
.brand-md{font-size:7px}.brand-md .brand-mark{width:12px;height:12px}
.brand-lg{font-size:10px}.brand-lg .brand-mark{width:20px;height:20px}
/* type */
.title{position:absolute;font-weight:800;text-transform:uppercase;letter-spacing:.2px;line-height:1.05}
.subtitle{position:absolute;font-size:4px}
.heading{position:absolute;left:12px;top:12px;font-size:8px;font-weight:800;text-transform:uppercase}
.heading::after{content:"";display:block;width:10px;height:1px;background:var(--red);margin-top:3px}
.tiny{font-size:2.8px;line-height:1.45;color:var(--text)}
.small{font-size:3.8px;line-height:1.3}
.footer{position:absolute;left:6px;bottom:5px;font-size:2.4px;color:var(--silver)}
.page-dot{position:absolute;right:6px;bottom:4px;width:5px;height:5px;border-radius:50%;background:var(--red)}
.white{color:var(--white)}.red{color:var(--red)}.grayt{color:var(--gray)}
.ico{display:inline-flex;align-items:center;justify-content:center;flex:none}
.ico svg{width:60%;height:60%}
.sq{width:7px;height:7px}
.circ{border-radius:50%}
.bg-red{background:var(--red)}.bg-black{background:var(--black)}.bg-gray{background:var(--gray)}.bg-silver{background:var(--silver)}.bg-dark{background:var(--dark)}
.item{position:absolute;display:flex;gap:3px;width:86px}
.item b{display:block;font-size:3.8px;font-weight:700}
.col-panel{position:absolute;top:0;bottom:0;padding:0 4px;text-align:center;color:var(--white)}
.col-panel h4{font-size:4px;font-weight:600;margin:4px 0 2px}
.col-panel p{font-size:2.5px;line-height:1.4;text-align:justify;opacity:.9}
.badge{position:absolute;background:#dadada}
</style>
</head>
<body>
<main class="pack">

<!-- 1 -->
<section class="slide">
  <div class="fill" role="img" aria-label="Jet airliner climbing through a grey cloudy sky" style="background:radial-gradient(circle at 28% 45%,#6f7378,#3a3d41 55%,#1f2124)"></div>
  <svg class="abs" style="left:0;top:0" width="296" height="165" viewBox="0 0 296 165"><path d="M135 140 A75 75 0 1 1 150 60" fill="none" stroke="#d9d9d9" stroke-width="7" opacity=".85"/></svg>
  <div class="title white" style="left:182px;top:84px;font-size:11px">Your Title Here</div>
  <div class="subtitle white" style="left:183px;top:101px">Your Subtitle Goes Here</div>
  <div class="brand brand-md" style="right:14px;top:136px"><span class="brand-mark"></span>LARKMOOR</div>
</section>

<!-- 2 -->
<section class="slide" style="background:#f4f4f4">
  <div class="abs circ" role="img" aria-label="Runway lights at sunset" style="left:-10px;top:-55px;width:200px;height:200px;background:radial-gradient(circle at 60% 65%,#f3b04a,#8e5a3a 40%,#24354a 75%)"></div>
  <svg class="abs" style="left:0;top:0" width="296" height="165" viewBox="0 0 296 165"><path d="M150 125 A88 88 0 1 1 178 40" fill="none" stroke="#cfcfcf" stroke-width="5"/></svg>
  <div class="title" style="left:182px;top:84px;font-size:11px;color:var(--dark)">Your Title Here</div>
  <div class="subtitle red" style="left:183px;top:101px">Your Subtitle Goes Here</div>
  <div class="brand brand-md" style="right:14px;top:136px"><span class="brand-mark"></span>LARKMOOR</div>
</section>

<!-- 3 -->
<section class="slide">
  <div class="fill" role="img" aria-label="Bright cloudy sky with an airliner in flight" style="background:linear-gradient(120deg,#fbfbfa,#ecebe8 50%,#d5d3cf)"></div>
  <div class="brand brand-md stack" style="left:30px;top:52px"><span class="brand-mark"></span>LARKMOOR</div>
  <div class="title" style="left:28px;top:97px;font-size:14px;color:var(--dark)">Your Title Here</div>
  <div class="abs bg-red" style="left:28px;right:0;top:93px;height:.7px;opacity:.6"></div>
  <div class="subtitle red" style="left:28px;top:115px">Your Subtitle Goes Here</div>
</section>

<!-- 4 -->
<section class="slide">
  <div class="fill" role="img" aria-label="Dark clouds with a faint airliner silhouette" style="background:radial-gradient(circle at 70% 40%,#505050,#2b2b2b 60%,#181818)"></div>
  <svg class="abs" style="left:0;top:0" width="296" height="165" viewBox="0 0 296 165"><circle cx="220" cy="80" r="62" fill="none" stroke="#777" stroke-width="6" opacity=".4"/></svg>
  <div class="brand brand-md stack" style="left:26px;top:22px"><span class="brand-mark"></span>LARKMOOR</div>
  <div class="title white" style="left:28px;top:107px;font-size:14px">Your Title Here</div>
  <div class="subtitle red" style="left:29px;top:126px">Your Subtitle Goes Here</div>
</section>

<!-- 5 -->
<section class="slide">
  <div class="fill" role="img" aria-label="Dark airport apron with a parked airliner" style="background:radial-gradient(circle at 40% 40%,#4b4b4b,#262626 60%,#151515)"></div>
  <svg class="abs" style="left:0;top:0" width="296" height="165" viewBox="0 0 296 165"><circle cx="80" cy="80" r="62" fill="none" stroke="#777" stroke-width="6" opacity=".4"/></svg>
  <div class="brand brand-md stack" style="right:14px;top:22px"><span class="brand-mark"></span>LARKMOOR</div>
  <div class="title white" style="right:16px;top:107px;font-size:14px">Your Title Here</div>
  <div class="subtitle red" style="right:16px;top:126px">Your Subtitle Goes Here</div>
</section>

<!-- 6 -->
<section class="slide">
  <div class="fill" role="img" aria-label="View from an aircraft window over a city at dusk" style="background:linear-gradient(180deg,#3a3a3a,#242424 60%,#3d3d3d)"></div>
  <div class="brand brand-lg stack" style="left:0;right:0;top:30px;align-items:center"><span class="brand-mark"></span>LARKMOOR</div>
  <div class="title white" style="left:0;right:0;top:92px;text-align:center;font-size:14px">Your Title Goes Here</div>
  <div class="subtitle white" style="left:0;right:0;top:110px;text-align:center">Your Subtitle Goes Here</div>
</section>

<!-- 7 agenda -->
<section class="slide">
  <div class="heading">Our Agenda</div>
  <div class="brand brand-sm stack" style="right:8px;top:8px"><span class="brand-mark"></span>LARKMOOR</div>
  <div class="item" style="left:40px;top:42px"><span class="ico sq bg-red"></span><div><b class="grayt" style="font-weight:400">Agenda One</b><span class="tiny red">10:00</span><p class="tiny">Short notes on the topic<br>and the aims for the day.</p></div></div>
  <div class="item" style="left:40px;top:76px"><span class="ico sq bg-black"></span><div><b class="grayt" style="font-weight:400">Agenda Two</b><span class="tiny red">11:00</span><p class="tiny">Short notes on the topic<br>and the aims for the day.</p></div></div>
  <div class="item" style="left:40px;top:110px"><span class="ico sq bg-red"></span><div><b class="grayt" style="font-weight:400">Agenda Three</b><span class="tiny red">12:00</span><p class="tiny">Short notes on the topic<br>and the aims for the day.</p></div></div>
  <div class="item" style="left:164px;top:42px"><span class="ico sq bg-black"></span><div><b class="grayt" style="font-weight:400">Agenda Four</b><span class="tiny red">13:00</span><p class="tiny">Short notes on the topic<br>and the aims for the day.</p></div></div>
  <div class="item" style="left:164px;top:76px"><span class="ico sq bg-red"></span><div><b class="grayt" style="font-weight:400">Agenda Five</b><span class="tiny red">14:00</span><p class="tiny">Short notes on the topic<br>and the aims for the day.</p></div></div>
  <div class="item" style="left:164px;top:110px"><span class="ico sq bg-black"></span><div><b class="grayt" style="font-weight:400">Agenda Six</b><span class="tiny red">15:00</span><p class="tiny">Short notes on the topic<br>and the aims for the day.</p></div></div>
  <div class="footer">© Copyright 2017 Larkmoor Systems Division. All rights reserved.</div><span class="page-dot"></span>
</section>

<!-- 8 featured -->
<section class="slide" style="background:var(--black)">
  <div class="abs" role="img" aria-label="Hands typing on a laptop" style="left:0;top:0;width:150px;height:165px;background:linear-gradient(135deg,#c9c9c9,#8f8f8f 55%,#5c5c5c)"></div>
  <div class="abs bg-red" style="left:150px;top:0;width:20px;height:165px"></div>
  <div class="title white" style="left:190px;top:18px;font-size:8px">Company<br>Featured<br>Product</div>
  <p class="abs tiny white" style="left:190px;top:66px;width:86px;color:#ddd"><b>Key point</b> our product keeps every trip on time and every team in touch, with clear tools built for travel staff across all of our offices.</p>
  <div class="abs" style="left:190px;top:108px;width:82px">
    <div class="tiny white" style="text-align:right;padding-right:12px">76%</div>
    <div style="height:1.5px;background:#555;position:relative"><div style="width:76%;height:100%;background:var(--red)"></div><span style="position:absolute;left:74%;top:-2px;width:5px;height:5px;border-radius:50%;background:var(--red)"></span></div>
    <div class="tiny" style="margin-top:2px;color:#bbb">Insert title here</div>
  </div>
  <div class="abs" style="left:190px;top:130px;width:82px">
    <div class="tiny white" style="text-align:right;padding-right:4px">91%</div>
    <div style="height:1.5px;background:#555;position:relative"><div style="width:91%;height:100%;background:var(--red)"></div><span style="position:absolute;left:89%;top:-2px;width:5px;height:5px;border-radius:50%;background:var(--red)"></span></div>
    <div class="tiny" style="margin-top:2px;color:#bbb">Insert title here</div>
  </div>
</section>

<!-- 9 bullets -->
<section class="slide">
  <div class="heading">Bullets Point 1 Level</div>
  <div class="brand brand-sm stack" style="right:8px;top:8px"><span class="brand-mark"></span>LARKMOOR</div>
  <div class="item" style="left:14px;top:47px"><span class="ico circ bg-black" style="width:3px;height:3px;margin-top:1px"></span><div><b>Your Text Here</b><p class="tiny">A short line of text about<br>this point goes in here.</p></div></div>
  <div class="item" style="left:106px;top:47px"><span class="ico circ bg-red" style="width:3px;height:3px;margin-top:1px"></span><div><b class="red">Your Text Here</b><p class="tiny">A short line of text about<br>this point goes in here.</p></div></div>
  <div class="item" style="left:198px;top:47px"><span class="ico circ bg-black" style="width:3px;height:3px;margin-top:1px"></span><div><b>Your Text Here</b><p class="tiny">A short line of text about<br>this point goes in here.</p></div></div>
  <div class="item" style="left:14px;top:99px"><span class="ico circ bg-black" style="width:3px;height:3px;margin-top:1px"></span><div><b>Your Text Here</b><p class="tiny">A short line of text about<br>this point goes in here.</p></div></div>
  <div class="item" style="left:106px;top:99px"><span class="ico circ bg-red" style="width:3px;height:3px;margin-top:1px"></span><div><b class="red">Your Text Here</b><p class="tiny">A short line of text about<br>this point goes in here.</p></div></div>
  <div class="item" style="left:198px;top:99px"><span class="ico circ bg-black" style="width:3px;height:3px;margin-top:1px"></span><div><b>Your Text Here</b><p class="tiny">A short line of text about<br>this point goes in here.</p></div></div>
  <div class="footer">© Copyright 2017 Larkmoor Systems Division. All rights reserved.</div><span class="page-dot"></span>
</section>

<!-- 10 mosaic -->
<section class="slide" style="display:grid;grid-template-columns:148px 148px;grid-template-rows:55px 55px 55px">
  <div class="bg-black" style="padding:5px 16px"><p class="small white" style="font-size:3.4px">Our teams plan and book travel for clients in many lands, and they rely on tools that are fast, clear and simple for every single trip.</p></div>
  <div role="img" aria-label="Hiker resting on a rocky ridge" style="background:linear-gradient(180deg,#a9b7c4,#8c7a63)"></div>
  <div role="img" aria-label="Sea of clouds seen from above" style="background:linear-gradient(180deg,#8fb6d8,#e6eef5)"></div>
  <div class="bg-red" style="padding:13px 16px"><p class="small white" style="font-size:3.4px">Our teams plan and book travel for clients in many lands, and they rely on tools that are fast, clear and simple for every single trip.</p></div>
  <div class="bg-gray" style="padding:5px 16px"><p class="small white" style="font-size:3.4px">Our teams plan and book travel for clients in many lands, and they rely on tools that are fast, clear and simple for every single trip.</p></div>
  <div role="img" aria-label="Hands holding a tablet" style="background:linear-gradient(135deg,#d8d8d8,#8a8a8a)"></div>
</section>

<!-- 11 four columns -->
<section class="slide">
  <div class="heading">Your Title Here</div>
  <div class="brand brand-sm stack" style="right:8px;top:8px"><span class="brand-mark"></span>LARKMOOR</div>
  <div class="col-panel bg-black" style="left:0;width:74px;top:64px;bottom:28px"><svg width="9" height="9" viewBox="0 0 10 10" style="margin-top:14px"><circle cx="5" cy="5" r="4" fill="none" stroke="#fff" stroke-width=".8"/><circle cx="5" cy="5" r="1.5" fill="#fff"/></svg><h4>Heading Here</h4><p>Short text for this column about our work and the aims we share with each team.</p></div>
  <div class="col-panel bg-red" style="left:74px;width:74px;top:64px;bottom:28px"><svg width="9" height="9" viewBox="0 0 10 10" style="margin-top:14px"><circle cx="5" cy="4" r="3" fill="none" stroke="#fff" stroke-width=".8"/><path d="M4 8h2" stroke="#fff" stroke-width=".8"/></svg><h4>Heading Here</h4><p>Short text for this column about our work and the aims we share with each team.</p></div>
  <div class="col-panel bg-gray" style="left:148px;width:74px;top:64px;bottom:28px"><svg width="9" height="9" viewBox="0 0 10 10" style="margin-top:14px"><circle cx="3" cy="3" r="2" fill="none" stroke="#fff" stroke-width=".8"/><circle cx="7" cy="7" r="2" fill="none" stroke="#fff" stroke-width=".8"/></svg><h4>Heading Here</h4><p>Short text for this column about our work and the aims we share with each team.</p></div>
  <div class="col-panel bg-silver" style="left:222px;width:74px;top:64px;bottom:28px"><svg width="9" height="9" viewBox="0 0 10 10" style="margin-top:14px"><rect x="1" y="2" width="8" height="6" fill="none" stroke="#fff" stroke-width=".8"/></svg><h4>Heading Here</h4><p>Short text for this column about our work and the aims we share with each team.</p></div>
  <div class="footer">© Copyright 2017 Larkmoor Systems Division. All rights reserved.</div><span class="page-dot"></span>
</section>

<!-- 12 divider -->
<section class="slide">
  <div class="abs bg-red" style="left:0;right:0;top:92px;height:.8px"></div>
  <div class="brand brand-md stack" style="right:24px;top:72px"><span class="brand-mark"></span></div>
  <div class="title" style="right:22px;top:100px;font-size:9px">Divider Page</div>
  <div class="subtitle red" style="right:22px;top:111px;font-size:3.4px">Subtitle Here</div>
  <p class="abs tiny" style="right:22px;top:117px;width:112px;text-align:right">A brief note to open the next part of the talk, with the main idea and what the team will see.</p>
</section>

<!-- 13 differences -->
<section class="slide">
  <div class="heading">Our Differences</div>
  <div class="brand brand-sm stack" style="right:8px;top:8px"><span class="brand-mark"></span>LARKMOOR</div>
  <div class="abs bg-black" style="left:16px;top:44px;width:266px;height:88px">
    <div class="abs" role="img" aria-label="Aircraft wing over the horizon at sunset" style="left:155px;top:12px;width:100px;height:64px;background:linear-gradient(180deg,#2f5f9e,#9cc3e6 55%,#f2b35a)"></div>
    <div class="abs" style="left:10px;top:12px;width:138px;display:grid;gap:7px">
      <div style="display:flex;gap:5px;align-items:center"><span class="ico circ bg-red" style="width:7px;height:7px"></span><p class="tiny white">A short line on what makes our service stand out,<br>set in plain words for the team.</p></div>
      <div style="display:flex;gap:5px;align-items:center"><span class="ico circ bg-red" style="width:7px;height:7px"></span><p class="tiny white">A second note on how we help every traveller<br>get where they need to go.</p></div>
      <div style="display:flex;gap:5px;align-items:center"><span class="ico circ bg-red" style="width:7px;height:7px"></span><p class="tiny white">A short line on what makes our service stand out,<br>set in plain words for the team.</p></div>
      <div style="display:flex;gap:5px;align-items:center"><span class="ico circ bg-red" style="width:7px;height:7px"></span><p class="tiny white">A second note on how we help every traveller<br>get where they need to go.</p></div>
    </div>
  </div>
  <div class="footer">© Copyright 2017 Larkmoor Systems Division. All rights reserved.</div><span class="page-dot"></span>
</section>

<!-- 14 text & bullets -->
<section class="slide">
  <div class="heading">Text &amp; Bullet Area</div>
  <div class="brand brand-sm stack" style="right:8px;top:8px"><span class="brand-mark"></span>LARKMOOR</div>
  <div class="abs" style="left:18px;top:46px;width:74px">
    <div class="small red" style="margin-bottom:4px">Heading Goes Here</div>
    <p class="tiny">This block holds a short text about the topic, with room for a few clear lines.</p>
    <p class="tiny" style="margin-top:3px">A second block sets out the next point in a few more plain words.</p>
    <p class="tiny" style="margin-top:3px">A last block closes the topic and leads on to the next slide.</p>
  </div>
  <div class="item" style="left:108px;top:46px"><span class="ico circ bg-red" style="width:8px;height:8px"></span><div><b class="red" style="font-weight:400">Your Text Here</b><p class="tiny">A short line of text goes here.</p></div></div>
  <div class="item" style="left:108px;top:70px"><span class="ico circ bg-black" style="width:8px;height:8px"></span><div><b style="font-weight:400">Your Text Here</b><p class="tiny">A short line of text goes here.</p></div></div>
  <div class="item" style="left:108px;top:94px"><span class="ico circ bg-gray" style="width:8px;height:8px"></span><div><b class="grayt" style="font-weight:400">Your Text Here</b><p class="tiny">A short line of text goes here.</p></div></div>
  <div class="item" style="left:108px;top:118px"><span class="ico circ bg-silver" style="width:8px;height:8px"></span><div><b class="grayt" style="font-weight:400">Your Text Here</b><p class="tiny">A short line of text goes here.</p></div></div>
  <div class="item" style="left:200px;top:46px"><span class="ico circ bg-silver" style="width:8px;height:8px"></span><div><b class="grayt" style="font-weight:400">Your Text Here</b><p class="tiny">A short line of text goes here.</p></div></div>
  <div class="item" style="left:200px;top:70px"><span class="ico circ bg-gray" style="width:8px;height:8px"></span><div><b class="grayt" style="font-weight:400">Your Text Here</b><p class="tiny">A short line of text goes here.</p></div></div>
  <div class="item" style="left:200px;top:94px"><span class="ico circ bg-black" style="width:8px;height:8px"></span><div><b style="font-weight:400">Your Text Here</b><p class="tiny">A short line of text goes here.</p></div></div>
  <div class="item" style="left:200px;top:118px"><span class="ico circ bg-red" style="width:8px;height:8px"></span><div><b class="red" style="font-weight:400">Your Text Here</b><p class="tiny">A short line of text goes here.</p></div></div>
  <div class="footer">© Copyright 2017 Larkmoor Systems Division. All rights reserved.</div><span class="page-dot"></span>
</section>

<!-- 15 clients -->
<section class="slide">
  <div class="badge" style="left:14px;top:16px;width:46px;height:18px;border-radius:2px"></div>
  <div class="badge circ" style="left:88px;top:12px;width:30px;height:26px"></div>
  <div class="badge" style="left:158px;top:16px;width:46px;height:16px;border-radius:2px"></div>
  <div class="badge" style="left:236px;top:16px;width:46px;height:14px;border-radius:2px"></div>
  <div class="badge circ" style="left:22px;top:60px;width:30px;height:30px"></div>
  <div class="badge" style="left:240px;top:75px;width:42px;height:6px;border-radius:3px"></div>
  <div class="badge circ" style="left:22px;top:122px;width:28px;height:28px"></div>
  <div class="badge circ" style="left:96px;top:122px;width:30px;height:30px"></div>
  <div class="badge" style="left:158px;top:124px;width:50px;height:22px;border-radius:2px"></div>
  <div class="badge circ" style="left:244px;top:120px;width:32px;height:32px"></div>
  <div class="abs bg-black" style="left:74px;top:55px;width:148px;height:54px;display:flex;align-items:center;justify-content:center;text-align:center">
    <div class="title white" style="position:static;font-size:12px">Our Awesome<br>Client</div>
  </div>
</section>

<!-- 16 five columns -->
<section class="slide">
  <div class="col-panel bg-black" style="left:0;width:60px"><svg width="16" height="16" viewBox="0 0 10 10" style="margin-top:40px"><circle cx="5" cy="5" r="4" fill="none" stroke="#fff" stroke-width=".5"/><circle cx="5" cy="5" r="1.6" fill="none" stroke="#fff" stroke-width=".5"/></svg><h4 style="font-size:5px;margin-top:22px">Heading Here</h4><p>Short text for this column about our work and the aims we share.</p></div>
  <div class="col-panel" style="left:60px;width:59px;background:#262626"><svg width="16" height="16" viewBox="0 0 10 10" style="margin-top:40px"><rect x="1.5" y="1.5" width="7" height="5.5" fill="none" stroke="#fff" stroke-width=".5"/><path d="M3 9h4" stroke="#fff" stroke-width=".5"/></svg><h4 style="font-size:5px;margin-top:22px">Heading Here</h4><p>Short text for this column about our work and the aims we share.</p></div>
  <div class="col-panel" style="left:119px;width:59px;background:#3b3b3b"><svg width="16" height="16" viewBox="0 0 10 10" style="margin-top:40px"><circle cx="4.5" cy="4.5" r="3" fill="none" stroke="#fff" stroke-width=".5"/><path d="M6.7 6.7L9 9" stroke="#fff" stroke-width=".6"/></svg><h4 style="font-size:5px;margin-top:22px">Heading Here</h4><p>Short text for this column about our work and the aims we share.</p></div>
  <div class="col-panel" style="left:178px;width:59px;background:#4d4d4d"><svg width="16" height="16" viewBox="0 0 10 10" style="margin-top:40px"><rect x="1.5" y="1.5" width="7" height="7" fill="none" stroke="#fff" stroke-width=".5"/><circle cx="5" cy="5" r="1.5" fill="none" stroke="#fff" stroke-width=".5"/></svg><h4 style="font-size:5px;margin-top:22px">Heading Here</h4><p>Short text for this column about our work and the aims we share.</p></div>
  <div class="col-panel bg-red" style="left:237px;width:59px"><svg width="16" height="16" viewBox="0 0 10 10" style="margin-top:40px"><circle cx="5" cy="5" r="4" fill="none" stroke="#fff" stroke-width=".5"/><circle cx="5" cy="5" r="2" fill="none" stroke="#fff" stroke-width=".5"/></svg><h4 style="font-size:5px;margin-top:22px">Heading Here</h4><p>Short text for this column about our work and the aims we share.</p></div>
</section>

<!-- 17 mockup -->
<section class="slide">
  <div class="heading">Our Mockup Area</div>
  <div class="brand brand-sm stack" style="right:8px;top:8px"><span class="brand-mark"></span>LARKMOOR</div>
  <div class="abs" style="left:0;right:0;top:95px;bottom:28px;background:#3a3a3a"></div>
  <div class="abs" role="img" aria-label="Laptop showing the company name on screen" style="left:70px;top:36px;width:158px;height:108px;background:linear-gradient(180deg,#efefef,#d4d4d4);border-radius:3px"></div>
  <div class="brand brand-md stack" style="left:0;right:0;top:70px;align-items:center"><span class="brand-mark"></span>LARKMOOR</div>
  <div class="abs bg-black tiny white" style="left:12px;top:62px;width:30px;padding:1px 3px">Your Text<br>Goes Here</div>
  <div class="abs bg-red tiny white" style="left:12px;top:85px;width:30px;padding:1px 3px">Your Text<br>Goes Here</div>
  <div class="abs bg-gray tiny white" style="left:12px;top:108px;width:30px;padding:1px 3px">Your Text<br>Goes Here</div>
  <div class="abs bg-gray tiny white" style="right:12px;top:62px;width:30px;padding:1px 3px">Your Text<br>Goes Here</div>
  <div class="abs bg-black tiny white" style="right:12px;top:85px;width:30px;padding:1px 3px">Your Text<br>Goes Here</div>
  <div class="abs bg-red tiny white" style="right:12px;top:108px;width:30px;padding:1px 3px">Your Text<br>Goes Here</div>
</section>

<!-- 18 right picture / chart -->
<section class="slide">
  <div class="abs bg-black" style="left:0;top:0;width:148px;height:165px"></div>
  <div class="abs circ" style="left:40px;top:28px;width:70px;height:70px;border:1.5px solid #fff;display:flex;align-items:center;justify-content:center;text-align:center">
    <div style="font-size:8px;line-height:1.2;color:#fff"><span class="red">RIGHT</span><br>PICTURE<br>SLIDE</div>
  </div>
  <p class="abs tiny" style="left:22px;top:118px;width:106px;text-align:center;color:#ddd">A short text that sits under the title and tells the team what the chart on the right side shows.</p>
  <svg class="abs" style="left:170px;top:30px" width="110" height="60" viewBox="0 0 110 60">
    <g fill="var(--red)"><rect x="4" y="14" width="3" height="42"/><rect x="30" y="22" width="3" height="34"/><rect x="56" y="18" width="3" height="38"/><rect x="82" y="10" width="3" height="46"/></g>
    <g fill="var(--black)"><rect x="9" y="28" width="3" height="28"/><rect x="35" y="6" width="3" height="50"/><rect x="61" y="30" width="3" height="26"/><rect x="87" y="20" width="3" height="36"/></g>
    <g fill="var(--silver)"><rect x="14" y="36" width="3" height="20"/><rect x="40" y="30" width="3" height="26"/><rect x="66" y="12" width="3" height="44"/><rect x="92" y="4" width="3" height="52"/></g>
  </svg>
  <div class="abs tiny" style="left:200px;top:91px">■ Sales ■ Market ■ Cost</div>
  <div class="abs" style="left:160px;top:100px;display:flex;align-items:center;gap:3px"><svg width="7" height="6" viewBox="0 0 7 6"><path d="M3.5 0L7 6H0z" fill="var(--red)"/></svg><span style="font-size:15px;font-weight:700">85%</span></div>
  <div class="abs" style="left:172px;top:121px;font-size:3.4px;font-weight:700">Profit</div>
  <p class="abs tiny" style="left:172px;top:126px;width:60px">Profit rose in each part of the year with strong sales.</p>
</section>

<!-- 19 divider left -->
<section class="slide">
  <div class="brand brand-md stack" style="left:34px;top:72px"><span class="brand-mark"></span></div>
  <div class="title" style="left:34px;top:98px;font-size:9px">Divider Page</div>
  <div class="subtitle red" style="left:34px;top:109px;font-size:3.4px">Subtitle Here</div>
  <p class="abs tiny" style="left:34px;top:115px;width:112px">A brief note to open the next part of the talk, with the main idea and what the team will see.</p>
</section>

<!-- 20 mockup dark -->
<section class="slide" style="background:var(--dark)">
  <div class="heading white">Our Mockup Area</div>
  <div class="abs" role="img" aria-label="Desktop monitor showing the company name on screen" style="left:128px;top:12px;width:152px;height:142px;background:linear-gradient(180deg,#f7f7f7,#cfcfcf);border-radius:3px"></div>
  <div class="brand brand-md stack" style="left:128px;width:152px;top:58px;align-items:center"><span class="brand-mark"></span>LARKMOOR</div>
  <div class="abs small" style="left:12px;top:38px;color:#ccc">Heading Here</div>
  <p class="abs tiny" style="left:12px;top:45px;width:104px;color:#bbb">A short text about the tools our staff use each day, and how they help book and plan every trip.</p>
  <div class="abs" style="left:12px;top:80px;width:104px;height:.6px;background:var(--red)"></div>
  <div class="abs" style="left:12px;top:89px;width:104px;display:flex;gap:4px"><span class="ico circ" style="width:7px;height:7px;background:#fff"></span><p class="tiny" style="color:#bbb">A short line about the first point, with a few words on what it means for our teams.</p></div>
  <div class="abs" style="left:12px;top:112px;width:104px;display:flex;gap:4px"><span class="ico circ bg-red" style="width:7px;height:7px"></span><p class="tiny" style="color:#bbb">A short line about the next point, with a few words on what it means for our teams.</p></div>
  <div class="footer">© Copyright 2017 Larkmoor Systems Division. All rights reserved.</div><span class="page-dot"></span>
</section>

<!-- 21 line chart -->
<section class="slide">
  <div class="title" style="left:24px;top:40px;font-size:9px">This is Line<br>Chart Slide</div>
  <div class="abs bg-red white" style="left:24px;top:72px;width:64px;height:8px;font-size:3.5px;display:flex;align-items:center;justify-content:center">Creative Text Here</div>
  <p class="abs tiny" style="left:24px;top:98px;width:70px"><span class="red">Short note</span> on the trend in this chart and what the two lines show for the year.</p>
  <svg class="abs" style="left:140px;top:28px" width="150" height="124" viewBox="0 0 150 124" font-family="Raleway, sans-serif" font-size="3" fill="#999">
    <g stroke="#eee" stroke-width=".5"><line x1="16" y1="6" x2="146" y2="6"/><line x1="16" y1="24" x2="146" y2="24"/><line x1="16" y1="42" x2="146" y2="42"/><line x1="16" y1="60" x2="146" y2="60"/><line x1="16" y1="78" x2="146" y2="78"/><line x1="16" y1="96" x2="146" y2="96"/><line x1="16" y1="114" x2="146" y2="114"/></g>
    <text x="8" y="7">4.5</text><text x="8" y="25">4.0</text><text x="8" y="43">3.5</text><text x="8" y="61">3.0</text><text x="8" y="79">2.5</text><text x="8" y="97">1.0</text><text x="8" y="115">0.0</text>
    <polyline points="26,28 58,60 90,34 124,70" fill="none" stroke="var(--black)" stroke-width="1.2"/>
    <polyline points="26,62 58,38 90,64 124,40" fill="none" stroke="var(--red)" stroke-width="1.2"/>
    <text x="20" y="121">Category 1</text><text x="52" y="121">Category 2</text><text x="84" y="121">Category 3</text><text x="118" y="121">Category 4</text>
  </svg>
  <div class="footer">© Copyright 2017 Larkmoor Systems Division. All rights reserved.</div><span class="page-dot"></span>
</section>

</main>
</body>
</html>
```